Postcard Design

Heating & Cooling

I want to create a post card for a Tune Up program that we offer customer for this spring.
Updates

I would like to change the date from April 1st - June 31st.
I would also like to change the size and go larger for the post card.

Keep the designs coming.
Thanks

I have decided to change the price of the cost of the program to "Only $99.00" due to other competitors pricing in my area.
If possible include at the bottom of the design > "Does not cover repair or parts" in a small font

Reason: We need more time for better designs. So I am extending the deadline by 7 days.

Target Market(s)

Residential Customers for Air Conditioning Tune Ups

Requirements
Must have
• We are promoting a tune up for the air conditioning system for $129.00.

The price is effective from April 1st - July 31st

I would like for the post card to be attention grabbing from the customers point of view. So mainly, add bold letting and everything to get attention.
Nice to have
• Also add to the card if possible:
Lower Energy Bills
Increase the life of your system
Prevent future breakdowns

Stay Cool this Summer with our Keystone Service Program

And add a logo that shows stacks of coins to indicate the money that can be saved

You also can look at other post cards that has been created for this particular program and design from it.

```html
<!DOCTYPE html>
<html lang="en">
<head>
<meta charset="utf-8">
<title>Stay Cool this Summer – Keystone Service Program</title>
<link rel="stylesheet" href="https://fonts.googleapis.com/css2?family=Baloo+2:wght@700;800&family=Mukta:wght@400;500&display=swap">
<style>
  :root {
    --paper: #ffffff;
    --ink-navy: #16213a;
    --accent-teal: #6aa9b0;
    --price-red: #c0222e;
    --band-navy: #15213a;
    --band-text: #f1ead6;
    --flame-deep: #1a0804;
    --flame-orange: #e8561a;
    --flame-yellow: #f6b42a;
    --smoke-deep: #0b0f3a;
    --smoke-blue: #3d4ccf;
    --smoke-pale: #aab6f0;
  }
  * { margin: 0; padding: 0; box-sizing: border-box; }
  html, body {
    width: 872px;
    height: 1200px;
    overflow: hidden;
    background: var(--paper);
  }
  .postcard {
    position: relative;
    width: 872px;
    height: 1200px;
    background: var(--paper);
    font-family: "Mukta", "Segoe UI", sans-serif;
    color: var(--ink-navy);
  }
  .hero-visual {
    position: absolute;
    left: 22px;
    top: 27px;
    width: 827px;
    height: 420px;
    background:
      radial-gradient(ellipse 28% 45% at 22% 45%, var(--flame-yellow) 0%, var(--flame-orange) 45%, transparent 75%),
      radial-gradient(ellipse 22% 35% at 78% 40%, var(--smoke-pale) 0%, var(--smoke-blue) 40%, transparent 80%),
      linear-gradient(90deg, var(--flame-deep) 0%, #2a0c05 40%, #05050f 52%, var(--smoke-deep) 65%, #141a5e 100%);
  }
  .headline {
    position: absolute;
    left: 0;
    right: 0;
    top: 455px;
    text-align: center;
    font-family: "Baloo 2", "Trebuchet MS", sans-serif;
    font-weight: 800;
    font-size: 68px;
    line-height: 1;
    letter-spacing: 0.5px;
    color: var(--ink-navy);
  }
  .subhead {
    position: absolute;
    right: 48px;
    top: 532px;
    font-family: "Mukta", "Segoe UI", sans-serif;
    font-weight: 500;
    font-size: 32px;
    line-height: 1;
    color: var(--accent-teal);
  }
  .price {
    position: absolute;
    left: 0;
    right: 0;
    top: 600px;
    text-align: center;
    font-family: "Baloo 2", "Trebuchet MS", sans-serif;
    font-weight: 800;
    font-size: 172px;
    line-height: 1;
    color: var(--price-red);
  }
  .benefits {
    position: absolute;
    left: 0;
    right: 0;
    top: 840px;
    list-style: none;
    text-align: center;
    font-size: 42px;
    line-height: 72px;
    font-weight: 400;
    color: var(--ink-navy);
  }
  .validity-band {
    position: absolute;
    left: 22px;
    top: 1075px;
    width: 827px;
    height: 82px;
    background: var(--band-navy);
    color: var(--band-text);
    display: flex;
    align-items: center;
    justify-content: center;
    font-family: "Baloo 2", "Trebuchet MS", sans-serif;
    font-weight: 700;
    font-size: 33px;
    padding-top: 6px;
  }
</style>
</head>
<body>
  <main class="postcard">
    <div class="hero-visual" role="img" aria-label="Swirling orange flames on the left meeting cool blue smoke on the right, on a black background"></div>
    <h1 class="headline">Stay Cool this Summer</h1>
    <p class="subhead">with our Keystone Service Program</p>
    <p class="price">$129.00.</p>
    <ul class="benefits">
      <li>Lower Energy Bills</li>
      <li>Increase the life of your system</li>
      <li>Prevent future breakdowns</li>
    </ul>
    <p class="validity-band">The price is effective from April 1st - July 31st</p>
  </main>
</body>
</html>
```